Online Bed Retailer needs a home page banner.

I need a web banner for the home page to my bed & mattress retail website.(www.slumbercrestoutlet.com) I wish to communicate to the general public my offer of FREE UK delivery with every order & interest FREE credit with all orders over £350.

Industry/Entity Type

Retail

```html
<!DOCTYPE html>
<html lang="en">
<head>
<meta charset="utf-8">
<title>Free Credit &amp; Free UK Delivery Banner</title>
<link rel="stylesheet" href="https://fonts.googleapis.com/css2?family=Montserrat:ital,wght@0,900;1,500&family=Barlow:wght@500;700&display=swap">
<style>
  :root {
    --paper: #ffffff;
    --brand-blue: #0b55a8;
    --outline-violet: #3b2fd6;
    --shade-blue: #07397a;
    --delivery-red: #e8202a;
    --ink-white: #ffffff;
    --trim: #000000;
    --photo-deep: #8a5a52;
    --photo-warm: #b89a7c;
    --photo-violet: #6a52c4;
    --photo-light: #e9e4dc;
  }
  * { margin: 0; padding: 0; box-sizing: border-box; }
  html, body { width: 1200px; height: 1000px; overflow: hidden; background: var(--paper); }
  .canvas { position: relative; width: 1200px; height: 1000px; background: var(--paper); }

  .trim-marks { position: absolute; inset: 0; }

  .banner {
    position: absolute; left: 38px; top: 322px;
    width: 1124px; height: 356px; overflow: hidden;
    background: var(--paper);
  }
  .delivery-photo {
    position: absolute; left: 0; top: 0; width: 690px; height: 282px;
    background: linear-gradient(90deg,
      var(--photo-deep) 0%,
      var(--photo-warm) 22%,
      #a98fb4 42%,
      var(--photo-light) 72%,
      rgba(255,255,255,0) 100%);
  }

  .credit-headline {
    position: absolute; right: 30px; top: 16px; width: 340px;
    font-family: "Montserrat", sans-serif; font-weight: 900;
    color: var(--brand-blue); text-align: center; line-height: .86;
    text-shadow:
      -2px 0 0 var(--outline-violet), 2px 0 0 var(--outline-violet),
      0 -2px 0 var(--outline-violet), 0 2px 0 var(--outline-violet),
      0 4px 0 var(--shade-blue), 0 5px 4px rgba(0,0,0,.25);
  }
  .credit-headline .word-free { display: block; font-size: 124px; letter-spacing: 1px; }
  .credit-headline .word-credit { display: block; font-size: 82px; margin-top: 4px; }

  .credit-terms { position: absolute; left: 612px; top: 198px; width: 512px; height: 60px; }
  .credit-terms svg { position: absolute; inset: 0; }
  .credit-terms p {
    position: relative; padding-left: 40px; line-height: 60px;
    font-family: "Montserrat", sans-serif; font-style: italic; font-weight: 500;
    font-size: 39px; color: var(--ink-white); white-space: nowrap;
  }

  .delivery-band {
    position: absolute; left: 0; top: 282px; width: 1124px; height: 74px;
    background: var(--delivery-red);
    font-family: "Barlow", sans-serif; font-weight: 500;
    font-size: 60px; line-height: 74px; letter-spacing: 2px;
    color: var(--ink-white); text-align: center; white-space: nowrap;
  }
  .delivery-band strong { font-weight: 700; }
</style>
</head>
<body>
<div class="canvas">
  <svg class="trim-marks" width="1200" height="1000" viewBox="0 0 1200 1000" aria-hidden="true">
    <g stroke="var(--trim)" stroke-width="1">
      <line x1="38.5" y1="292" x2="38.5" y2="313"/>
      <line x1="1161.5" y1="292" x2="1161.5" y2="313"/>
      <line x1="38.5" y1="687" x2="38.5" y2="708"/>
      <line x1="1161.5" y1="687" x2="1161.5" y2="708"/>
      <line x1="8" y1="322.5" x2="30" y2="322.5"/>
      <line x1="1170" y1="322.5" x2="1192" y2="322.5"/>
      <line x1="8" y1="677.5" x2="30" y2="677.5"/>
      <line x1="1170" y1="677.5" x2="1192" y2="677.5"/>
    </g>
  </svg>

  <section class="banner">
    <div class="delivery-photo" role="img" aria-label="Photo of a delivery man in a purple cap and polo shirt unloading a plastic-wrapped mattress from a van"></div>

    <h1 class="credit-headline">
      <span class="word-free">FREE</span>
      <span class="word-credit">CREDIT</span>
    </h1>

    <div class="credit-terms">
      <svg width="512" height="60" viewBox="0 0 512 60" aria-hidden="true">
        <polygon points="40,0 512,0 512,60 0,60" fill="var(--brand-blue)"/>
      </svg>
      <p>on all order over £350</p>
    </div>

    <p class="delivery-band"><strong>FREE</strong> UK DELIVERY ON ALL ORDERS</p>
  </section>
</div>
</body>
</html>
```